SINGLE PAGE WEBSITE needed for Haunted-House Style Horror Event!

PROJECT:
Single page website to advertise "Midnight Fever"

ABOUT MIDNIGHT FEVER:
Midnight Fever is a Horror Experience event, that will be held on June 1st 2019 at The Lantern Hall in Sydney.

At the event, patrons will enter 6 different rooms and have a horror experience in each one.

There's a bar on-site for them to drink as well.

NEEDS FOR THE WEBSITE:
1. Video banner at top, and scrolling photos after video finishes, and text over the top of the video with the name and date of the event
eg.
"A Night of Immersive Horror Experiences"
"The Lantern Hall | June 1st, 2019"

2. Multiple Book Now buttons on the page, which will link to an external booking platform

3. It should say somewhere "Produced by [BRIGHT HOLLOW PRODUCTIONS LOGO]"

4. A "Next Steps" section that has the steps for them to complete, such as
- Purchase your ticket HERE for one of our waves
- Rock up at the Lantern Hall on June 1st at your wave time
- Experience each of our 6 Interactive Horror Rooms
- Grab some drinks at the bar, a bite to eat, and enjoy a fantastic night out!

Other things that should be included somewhere:
- Testimonials
- FAQs (maybe as a dropdown, so it doesn't take up much space?)
- Contact Form on Footer

- - - -

Images, logos, and more attached!

• 1. Video banner at top, and scrolling photos after video finishes, and text over the top of the video with the name and date of the event
• eg.
• "A Night of Immersive Horror Experiences"
• "The Lantern Hall | June 1st, 2019"
• 2. multiple Book Now buttons on the page, which will link to an external booking platform
• 3. It should say somewhere "Produced by [Bright Hollow Productions LOGO]" with the Bright Hollow logo
• 4. A "Next Steps" section that has the steps for them to complete, such as
• - Purchase your ticket HERE for one of our waves
• - Rock up at the Lantern Hall on June 1st at your wave time
• - Experience each of our 6 Interactive Horror Rooms
• - Grab some drinks at the bar, a bite to eat, and enjoy a fantastic night out!
• Other things that should be included somewhere:
• - Testimonials
• - FAQs (maybe as a dropdown, so it doesn't take up much space?)
• - Contact Form on Footer

```html
<!DOCTYPE html>
<html lang="en">
<head>
<meta charset="utf-8">
<title>Midnight Fever — A Night of Immersive Horror Experiences</title>
<link href="https://fonts.googleapis.com/css2?family=Creepster&family=Arimo:wght@400;700&family=Montserrat:wght@500;700&display=swap" rel="stylesheet">
<style>
  :root{
    --canvas:#ffffff;
    --page:#0a0a0a;
    --blood:#e0201f;
    --slime:#8dc63f;
    --slime-button:#7ab03a;
    --text:#ffffff;
    --line:#8a8a8a;
  }
  *{box-sizing:border-box;margin:0;padding:0}
  html,body{width:1200px;height:1200px;overflow:hidden;background:var(--canvas)}
  body{position:relative;font-family:"Arimo",Arial,sans-serif;color:var(--text)}
  .page{position:absolute;left:436px;top:12px;width:410px;height:1470px;background:var(--page);transform:scale(.8);transform-origin:0 0;overflow:hidden}
  .abs{position:absolute}
  .photo{position:absolute}

  /* header / hero */
  .hero{left:0;top:0;width:410px;height:212px;background:radial-gradient(ellipse at 55% 35%,#3d3a33 0%,#22201c 45%,#0d0d0c 100%)}
  .brand{left:12px;top:8px;font-family:"Montserrat",sans-serif;font-weight:700;font-size:7px;color:var(--slime);display:flex;align-items:center;gap:4px;white-space:nowrap}
  .brand i{display:block;width:8px;height:8px;border-radius:50%;background:var(--slime)}
  .nav{left:113px;top:11px;display:flex;gap:10px;font-family:"Montserrat",sans-serif;font-weight:500;font-size:5.2px;color:var(--text);white-space:nowrap}
  .nav .active{color:var(--blood)}
  .btn-red{left:338px;top:7px;width:49px;height:15px;background:var(--blood);font-family:"Montserrat",sans-serif;font-weight:700;font-size:5px;display:flex;align-items:center;justify-content:center;letter-spacing:.4px}
  .play{left:191px;top:81px}
  .hero-title{left:0;width:410px;top:127px;text-align:center;font-family:"Creepster",cursive;font-size:12.5px;letter-spacing:.8px;color:var(--blood)}
  .hero-sub{left:0;width:410px;top:152px;text-align:center;font-size:7.5px;letter-spacing:.6px;color:var(--text)}
  .btn-green{background:var(--slime-button);font-family:"Montserrat",sans-serif;font-weight:700;font-size:4.6px;letter-spacing:.4px;display:flex;align-items:center;justify-content:center;color:var(--text)}

  .section-title{left:0;width:410px;text-align:center;font-family:"Creepster",cursive;font-size:12px;letter-spacing:.8px;color:var(--slime)}

  /* welcome */
  .welcome-title{left:213px;top:257px;width:150px;font-size:10px;font-weight:700;letter-spacing:1px;line-height:1.25}
  .welcome-list{left:225px;top:302px;width:112px;list-style:none}
  .welcome-list li{position:relative;font-size:3.4px;line-height:1.45;color:var(--blood);margin-bottom:13px}
  .welcome-list li b{position:absolute;left:-6px;top:-1px;font-size:5px;color:var(--text);font-weight:700}

  /* rooms */
  .room-label{position:absolute;left:4px;top:2px;font-size:5.5px;font-weight:700;color:var(--text)}
  .step-caption{font-size:3.6px;line-height:1.3;color:var(--text);width:66px}

  /* testimonial */
  .quote-mark{left:222px;top:912px;font-family:Georgia,serif;font-size:20px;font-weight:700;color:var(--blood)}
  .quote{left:237px;top:922px;width:104px;font-size:4.4px;line-height:1.2}
  .quote-name{left:237px;top:946px;font-family:Georgia,serif;font-size:5px;font-weight:700;color:var(--blood)}

  /* faq */
  .faq-sub{left:0;width:382px;top:1066px;text-align:center;font-size:7.5px}
  .faq-item{width:130px;height:20px;border:1px solid var(--line);display:flex;align-items:center;justify-content:space-between;padding:0 5px;font-size:5.2px;white-space:nowrap}
  .faq-item svg{flex:none}

  /* contact */
  .contact{left:0;top:1206px;width:410px;height:136px;background:radial-gradient(ellipse at 45% 45%,#a82a24 0%,#8a1d19 45%,#4a0d0b 100%);border-top:1px solid #b03a30}
  .field-label{font-size:6px;letter-spacing:.5px}
  .field-line{height:1px;background:rgba(255,255,255,.25)}
  .message-box{left:69px;top:1284px;width:214px;height:54px;border:1px solid rgba(255,255,255,.35);padding:8px 3px;font-size:6px;letter-spacing:.5px}
  .send{left:293px;top:1299px;width:46px;height:25px;background:var(--slime-button);font-family:"Montserrat",sans-serif;font-weight:700;font-size:7px;letter-spacing:.6px;display:flex;align-items:center;justify-content:center}

  /* footer */
  .footer{left:0;top:1342px;width:410px;height:128px;background:var(--page)}
  .footer-brand{left:76px;top:1350px;font-family:"Montserrat",sans-serif;font-weight:700;font-size:5.5px;color:var(--slime);display:flex;align-items:center;gap:2px;white-space:nowrap}
  .footer-brand i{display:block;width:5px;height:5px;border-radius:50%;background:var(--slime)}
  .foot-head{font-size:4.4px;font-weight:700;letter-spacing:.5px}
  .foot-menu{list-style:none;font-size:4.4px;font-weight:700;line-height:8.6px;letter-spacing:.3px}
  .foot-menu .active{color:var(--blood)}
  .foot-address{font-size:4.4px;line-height:8.6px;color:#cfcf3a}
  .foot-address .plain{color:var(--text)}
  .foot-address .mail{color:#3a8fd8}
  .social{display:flex;gap:9px}
  .social i{display:block;width:8px;height:8px;border-radius:50%;background:var(--slime-button)}
  .bottom-bar{left:0;top:1447px;width:410px;height:23px;background:#050505}
  .copyright{left:0;width:410px;top:1456px;text-align:center;font-size:4.4px;color:var(--blood)}
</style>
</head>
<body>
<div class="page">

  <!-- Hero -->
  <div class="abs hero" role="img" aria-label="Video banner: costumed horror actors in a candlelit gothic room"></div>
  <div class="abs brand"><i></i>MIDNIGHT FEVER</div>
  <nav class="abs nav">
    <span class="active">Home</span><span>Rooms</span><span>How it works?</span><span>Testimonials</span><span>FAQs</span><span>Contact us</span>
  </nav>
  <div class="abs btn-red">BOOK NOW</div>
  <svg class="abs play" width="28" height="28" viewBox="0 0 28 28" aria-label="Play video">
    <circle cx="14" cy="14" r="14" fill="#fff"/>
    <path d="M11 8.5 L20 14 L11 19.5 Z" fill="#111"/>
  </svg>
  <div class="abs hero-title">A NIGHT OF IMMERSIVE HORROR EXPERIENCES"</div>
  <div class="abs hero-sub">" THE LANTERN HALL | JUNE 1ST,2019"</div>
  <div class="abs btn-green" style="left:181px;top:174px;width:48px;height:14px">BOOK NOW</div>

  <!-- Welcome -->
  <div class="abs section-title" style="top:230px">WELCOME!</div>
  <div class="photo" style="left:70px;top:272px;width:139px;height:123px;background:linear-gradient(120deg,#8e1418 0%,#5a0d12 40%,#2b3a44 70%,#131b20 100%)" role="img" aria-label="Costumed ghoul in a red-lit escape room"></div>
  <h2 class="abs welcome-title">PRIVATE ESCAPE ROOM ADVENTURES</h2>
  <ol class="abs welcome-list">
    <li><b>1.</b>Locked rooms set in a dark story world, where every clue hides a secret and the clock is always running out.</li>
    <li><b>2.</b>Solve the riddles with your group, find hidden keys and escape before the lights go out for good.</li>
    <li><b>3.</b>Live actors, eerie sounds and creeping shadows follow every step you take inside.</li>
  </ol>

  <!-- Rooms -->
  <div class="abs section-title" style="top:430px">OUR ROOMS</div>

  <div class="photo" style="left:69px;top:450px;width:86px;height:86px;background:linear-gradient(160deg,#6f9ac0 0%,#a58f74 55%,#4a3b2e 100%)" role="img" aria-label="Room 1: costumed actor in a field set"><span class="room-label">ROOM 1</span></div>
  <div class="photo" style="left:163px;top:450px;width:86px;height:86px;background:linear-gradient(160deg,#3a3c3a 0%,#1a1a1a 60%,#2b2b27 100%)" role="img" aria-label="Room 2: hooded ghost"><span class="room-label">ROOM 2</span></div>
  <div class="photo" style="left:257px;top:450px;width:86px;height:86px;background:linear-gradient(160deg,#2a3448 0%,#3a2c30 55%,#151519 100%)" role="img" aria-label="Room 3: costumed horror actor under a spotlight"><span class="room-label">ROOM 3</span></div>

  <div class="abs btn-green" style="left:88px;top:540px;width:48px;height:14px">BOOK NOW</div>
  <div class="abs btn-green" style="left:182px;top:540px;width:48px;height:14px">BOOK NOW</div>
  <div class="abs btn-green" style="left:276px;top:540px;width:48px;height:14px">BOOK NOW</div>

  <div class="photo" style="left:69px;top:568px;width:86px;height:86px;background:linear-gradient(160deg,#12305a 0%,#3a4660 50%,#1b1b24 100%)" role="img" aria-label="Room 4: zombie twins"><span class="room-label">ROOM 4</span></div>
  <div class="photo" style="left:163px;top:568px;width:86px;height:86px;background:linear-gradient(160deg,#2e5378 0%,#8a9aa8 50%,#20252c 100%)" role="img" aria-label="Room 5: pale ghoul with white hair"><span class="room-label">ROOM 5</span></div>
  <div class="photo" style="left:257px;top:568px;width:86px;height:86px;background:linear-gradient(160deg,#0d1320 0%,#3a2a2a 50%,#7a3d3a 100%)" role="img" aria-label="Room 6: two possessed women in the dark"><span class="room-label">ROOM 6</span></div>

  <div class="abs btn-green" style="left:88px;top:658px;width:48px;height:14px">BOOK NOW</div>
  <div class="abs btn-green" style="left:182px;top:658px;width:48px;height:14px">BOOK NOW</div>
  <div class="abs btn-green" style="left:276px;top:658px;width:48px;height:14px">BOOK NOW</div>

  <!-- How it works -->
  <div class="abs section-title" style="top:694px">HOW IT WORKS?</div>
  <div class="photo" style="left:69px;top:728px;width:66px;height:77px;background:#e8c98a" role="img" aria-label="Event tickets"></div>
  <div class="photo" style="left:138px;top:728px;width:65px;height:77px;background:linear-gradient(160deg,#4a5a4e 0%,#6b4a3a 60%,#2a2420 100%)" role="img" aria-label="Theatre entrance"></div>
  <div class="photo" style="left:206px;top:728px;width:66px;height:77px;background:linear-gradient(160deg,#2a1610 0%,#4a2418 50%,#120a08 100%)" role="img" aria-label="Dark interactive horror room"></div>
  <div class="photo" style="left:276px;top:728px;width:66px;height:77px;background:linear-gradient(160deg,#3a2418 0%,#8a4a2a 50%,#1a4a6a 100%)" role="img" aria-label="Colourful drinks at the bar"></div>
  <div class="abs step-caption" style="left:69px;top:810px">PURCHASE YOUR<br>TICKETS HERE</div>
  <div class="abs step-caption" style="left:138px;top:810px">LANTERN HALL ON<br>JUNE 1st</div>
  <div class="abs step-caption" style="left:207px;top:810px">OUR 6 INTERACTIVE<br>HORROR ROOMS</div>
  <div class="abs step-caption" style="left:277px;top:810px;width:80px">GRAB SOME DRINKS AT THE BAR<br>AND ENJOY A FANTASTIC NIGHT OUT</div>

  <!-- Testimonials -->
  <div class="abs section-title" style="top:866px">TESTIMONIALS</div>
  <div class="photo" style="left:38px;top:900px;width:170px;height:98px;background:linear-gradient(150deg,#3a3a3e 0%,#4a3a30 50%,#1a1a1c 100%)" role="img" aria-label="Friends solving a puzzle on the floor of an escape room"></div>
  <div class="abs quote-mark">“</div>
  <p class="abs quote">"My friends had a super fun time deciphering puzzles and clues at Hollow Door. Thank you for hosting the event! We plan to return when you have new games set up."</p>
  <div class="abs quote-name">Mara Quill</div>

  <!-- FAQ -->
  <div class="abs section-title" style="top:1049px;width:400px">FAQ</div>
  <div class="abs faq-sub">FIND ANSWERS TO ALL OF YOUR QUESTIONS</div>

  <div class="abs faq-item" style="left:69px;top:1085px"><span>What is this?</span><svg width="6" height="4" viewBox="0 0 6 4"><path d="M.5 .5 3 3 5.5 .5" fill="none" stroke="#e0201f" stroke-width="1"/></svg></div>
  <div class="abs faq-item" style="left:211px;top:1085px"><span>Is this a hunted house?</span><svg width="6" height="4" viewBox="0 0 6 4"><path d="M.5 .5 3 3 5.5 .5" fill="none" stroke="#e0201f" stroke-width="1"/></svg></div>
  <div class="abs faq-item" style="left:69px;top:1113px"><span>If i'm late, can I still play?</span><svg width="6" height="4" viewBox="0 0 6 4"><path d="M.5 .5 3 3 5.5 .5" fill="none" stroke="#e0201f" stroke-width="1"/></svg></div>
  <div class="abs faq-item" style="left:211px;top:1113px"><span>Are there any age resetriction?</span><svg width="6" height="4" viewBox="0 0 6 4"><path d="M.5 .5 3 3 5.5 .5" fill="none" stroke="#e0201f" stroke-width="1"/></svg></div>
  <div class="abs faq-item" style="left:69px;top:1142px"><span>I need to reseduled my reservation!</span><svg width="6" height="4" viewBox="0 0 6 4"><path d="M.5 .5 3 3 5.5 .5" fill="none" stroke="#e0201f" stroke-width="1"/></svg></div>
  <div class="abs faq-item" style="left:211px;top:1142px"><span>Do I have arrive in advance?</span><svg width="6" height="4" viewBox="0 0 6 4"><path d="M.5 .5 3 3 5.5 .5" fill="none" stroke="#e0201f" stroke-width="1"/></svg></div>
  <div class="abs faq-item" style="left:69px;top:1171px"><span>How much does it cost?</span><svg width="6" height="4" viewBox="0 0 6 4"><path d="M.5 .5 3 3 5.5 .5" fill="none" stroke="#e0201f" stroke-width="1"/></svg></div>
  <div class="abs faq-item" style="left:211px;top:1171px"><span>It is scary?</span><svg width="6" height="4" viewBox="0 0 6 4"><path d="M.5 .5 3 3 5.5 .5" fill="none" stroke="#e0201f" stroke-width="1"/></svg></div>

  <!-- Contact -->
  <div class="abs contact" role="img" aria-label="Red-tinted shadowy figure behind the contact form"></div>
  <div class="abs section-title" style="top:1215px;width:400px">CONTACT US</div>
  <div class="abs field-label" style="left:72px;top:1241px">Name</div>
  <div class="abs field-line" style="left:69px;top:1253px;width:214px"></div>
  <div class="abs field-label" style="left:72px;top:1260px">Email Address</div>
  <div class="abs field-line" style="left:69px;top:1272px;width:214px"></div>
  <div class="abs message-box">Message</div>
  <div class="abs send">send</div>

  <!-- Footer -->
  <div class="abs footer"></div>
  <div class="abs footer-brand"><i></i>MIDNIGHT FEVER</div>
  <div class="abs foot-head" style="left:113px;top:1365px">MENU</div>
  <ul class="abs foot-menu" style="left:113px;top:1378px">
    <li class="active">Home</li><li>Rooms</li><li>How it works?</li><li>Testimonials</li><li>FAQs</li><li>Contact us</li>
  </ul>
  <div class="abs foot-head" style="left:179px;top:1365px">OUR ADDRESS</div>
  <div class="abs foot-address" style="left:178px;top:1378px">
    Lantern Events Ltd.<br>418 Ember Lane, Suite 12<br>Eastgate, NSW 2044<br>
    <span class="plain">Email:</span> <span class="mail">hello@lanternevents.com</span><br>
    <span class="plain">Tel: +61 2 5550 0142</span>
  </div>
  <div class="abs foot-head" style="left:272px;top:1365px">SOCIAL LINKS</div>
  <div class="abs social" style="left:273px;top:1378px"><i></i><i></i><i></i><i></i></div>
  <div class="abs bottom-bar"></div>
  <div class="abs copyright">Midnight Fever @ 2019 . All rights reserved</div>

</div>
</body>
</html>
```